Marlowe Candles scented candles made from soy wax

I want to make my Squarespace website look more professional. I need a website with an online store and workshops for my business with scented candles made from soy wax, wax melts, room fragrances, car fragrances, fragrance lamps and accessories. The design of the website should match my candle labels. The flower and the Marlowe Candles font must be in the logo. My current website: www.marlowecandles.ch

```html
<!DOCTYPE html>
<html lang="en">
<head>
<meta charset="utf-8">
<title>Marlowe Candles – Shop – Fragrance Lamps</title>
<link rel="stylesheet" href="https://fonts.googleapis.com/css2?family=Lato:wght@400;700&family=Oswald:wght@400;500;700&display=swap">
<style>
  :root{
    --gold:#8c6d1f;
    --ink:#2a2622;
    --muted:#6f6a63;
    --hero-dark:#2e1a12;
    --hero-mid:#5a3422;
    --footer-bg:#f3efe3;
    --white:#ffffff;
    --line:#d9d3c4;
  }
  *{box-sizing:border-box;margin:0;padding:0}
  html,body{width:1200px;height:2168px;overflow:hidden;background:var(--white)}
  body{font-family:"Lato",sans-serif;color:var(--ink);position:relative}

  .site-header{position:absolute;top:0;left:0;width:1200px;height:120px}
  .main-nav{position:absolute;left:100px;top:48px;display:flex;gap:34px;font-size:15px;color:var(--ink)}
  .main-nav a{color:inherit;text-decoration:none}
  .main-nav .active{border-bottom:1px solid var(--ink);padding-bottom:3px}
  .brand{position:absolute;left:0;width:1200px;top:26px;text-align:center}
  .brand-dot{display:block;width:34px;height:34px;border-radius:50%;background:var(--ink);margin:0 auto 6px}
  .brand-name{font-family:"Oswald",sans-serif;font-weight:500;font-size:26px;letter-spacing:1px;color:var(--ink);text-transform:uppercase}
  .header-icons{position:absolute;right:92px;top:44px;display:flex;gap:12px}
  .icon-btn{width:28px;height:28px;border-radius:50%;background:var(--gold);display:flex;align-items:center;justify-content:center}

  .hero{position:absolute;top:120px;left:0;width:1200px;height:360px;background:linear-gradient(90deg,var(--hero-dark) 0%,var(--hero-dark) 55%,var(--hero-mid) 100%)}
  .hero-photo{position:absolute;right:0;top:0;width:560px;height:360px;background:radial-gradient(circle at 45% 65%,#f6c87a 0%,#b8753a 18%,#6a3e24 45%,rgba(46,26,18,0) 80%),linear-gradient(90deg,rgba(46,26,18,1) 0%,#7b5236 60%,#9a7560 100%)}
  .hero-title{position:absolute;left:80px;top:138px;font-family:"Oswald",sans-serif;font-weight:700;font-size:68px;color:var(--white);letter-spacing:1px}
  .breadcrumb{position:absolute;left:80px;top:254px;font-family:"Oswald",sans-serif;font-size:17px;color:var(--white);text-transform:uppercase;font-weight:500}

  .product-grid{position:absolute;top:560px;left:112px;width:976px;display:grid;grid-template-columns:repeat(3,316px);column-gap:14px;row-gap:0}
  .product{height:444px;text-align:center}
  .product-image{width:316px;height:324px;background:linear-gradient(135deg,#6e5f52,#b4a79a 55%,#d9d0c6)}
  .product-image.light{background:linear-gradient(135deg,#8a7c70,#d8d2cb 55%,#efebe6)}
  .product-image.pink{background:linear-gradient(135deg,#6b5a50,#d9b7b0 55%,#e6dcd5)}
  .product-name{margin-top:42px;font-family:"Oswald",sans-serif;font-weight:500;font-size:15px;text-transform:uppercase;letter-spacing:.3px}
  .product-price{margin-top:6px;font-size:13px;color:var(--gold)}

  .site-footer{position:absolute;top:1912px;left:0;width:1200px;height:256px;background:var(--footer-bg)}
  .footer-links{position:absolute;left:112px;top:68px;list-style:none;font-size:15px;color:var(--gold);line-height:34px}
  .signup-label{position:absolute;left:664px;top:62px;font-size:12px;color:var(--muted)}
  .email-field{position:absolute;left:664px;top:96px;width:256px;height:40px;border:1px solid var(--line);background:var(--white);font-size:12px;color:var(--muted);padding:12px 14px}
  .subscribe-btn{position:absolute;left:940px;top:96px;width:148px;height:40px;background:var(--gold);color:var(--white);font-size:13px;font-weight:700;display:flex;align-items:center;justify-content:center}
  .social{position:absolute;left:944px;top:152px;display:flex;gap:12px}
  .social span{width:28px;height:28px;border-radius:50%;background:var(--gold);display:block}
  .copyright{position:absolute;left:0;width:1200px;top:218px;text-align:center;font-size:12px;color:var(--muted)}
  .currency{position:absolute;right:24px;top:238px;font-size:11px;color:var(--muted)}
</style>
</head>
<body>
  <header class="site-header">
    <nav class="main-nav">
      <a class="active">Shop</a><a>POS</a><a>Soy Wax</a><a>About MC</a><a>Workshop</a>
    </nav>
    <div class="brand"><span class="brand-dot"></span><div class="brand-name">Marlowe Candles</div></div>
    <div class="header-icons">
      <span class="icon-btn"><svg width="14" height="14" viewBox="0 0 14 14"><circle cx="6" cy="6" r="4" fill="none" stroke="#fff" stroke-width="1.8"/><line x1="9" y1="9" x2="13" y2="13" stroke="#fff" stroke-width="1.8"/></svg></span>
      <span class="icon-btn"><svg width="14" height="14" viewBox="0 0 14 14"><circle cx="7" cy="4.5" r="3" fill="#fff"/><path d="M1.5 13a5.5 5 0 0 1 11 0z" fill="#fff"/></svg></span>
      <span class="icon-btn"><svg width="14" height="14" viewBox="0 0 14 14"><path d="M3 5h8l-1 8H4z" fill="#fff"/><path d="M5 5V3.5a2 2 0 0 1 4 0V5" fill="none" stroke="#fff" stroke-width="1.4"/></svg></span>
    </div>
  </header>

  <section class="hero">
    <div class="hero-photo" role="img" aria-label="Lit candles beside rolled towels and a green leaf"></div>
    <h1 class="hero-title">SHOP</h1>
    <div class="breadcrumb">Shop &gt; Fragrance Lamps</div>
  </section>

  <main class="product-grid">
    <div class="product"><div class="product-image light" role="img" aria-label="White fragrance lamp with heart cut-out"></div><div class="product-name">Fragrance Lamp Heart</div><div class="product-price">CHF 15.00</div></div>
    <div class="product"><div class="product-image" role="img" aria-label="Grey fragrance lamp lettered Family"></div><div class="product-name">Fragrance Lamp Grey Family</div><div class="product-price">CHF 16.00</div></div>
    <div class="product"><div class="product-image light" role="img" aria-label="Square grey fragrance lamp"></div><div class="product-name">Fragrance Lamp Square Grey</div><div class="product-price">CHF 16.00</div></div>
    <div class="product"><div class="product-image" role="img" aria-label="Grey fragrance lamp with wave pattern"></div><div class="product-name">Fragrance Lamp Waves</div><div class="product-price">CHF 16.00</div></div>
    <div class="product"><div class="product-image pink" role="img" aria-label="Glossy pink fragrance lamp lettered Home"></div><div class="product-name">Fragrance Lamp Home Glanz</div><div class="product-price">CHF 16.00</div></div>
    <div class="product"><div class="product-image light" role="img" aria-label="White fragrance lamp lettered Love with wax melts"></div><div class="product-name">Duftlampe Love Weiss</div><div class="product-price">CHF 16.00</div></div>
    <div class="product"><div class="product-image light" role="img" aria-label="White butterfly pattern fragrance lamp on wooden base"></div><div class="product-name">Fragrance Lamp Butterfly White</div><div class="product-price">CHF 16.00</div></div>
    <div class="product"><div class="product-image light" role="img" aria-label="White perforated fragrance lamp"></div><div class="product-name">Duftlampe Weiss</div><div class="product-price">CHF 16.00</div></div>
  </main>

  <footer class="site-footer">
    <ul class="footer-links"><li>Pos</li><li>Soy Wax</li><li>About Mc</li><li>Workshop</li><li>Conditions</li></ul>
    <div class="signup-label">Sign up to receive news and updates</div>
    <div class="email-field">Email Address</div>
    <div class="subscribe-btn">Subscribe Here</div>
    <div class="social"><span></span><span></span><span></span></div>
    <div class="copyright">(c) Copyright 2020. All Rights Reserved</div>
    <div class="currency">CHF</div>
  </footer>
</body>
</html>
```